KLT Roofing Pty Ltd

We are a high end residential Roofing company
We would like something silimar to the attached logo with the same color scheme

Target Market(s)

High end residential Builders & Architects

Industry/Entity Type

Residential

```html
<!DOCTYPE html>
<html lang="en">
<head>
<meta charset="utf-8">
<title>KLT Roofing – Business Cards</title>
<link href="https://fonts.googleapis.com/css2?family=Open+Sans:wght@400;700&display=swap" rel="stylesheet">
<style>
  :root {
    --bg: #e6e6e4;
    --card: #ffffff;
    --brand-blue: #0f9bce;
    --brand-slate: #3b4a57;
    --text-grey: #4a4f55;
    --icon-blue: #5aa9d6;
  }
  * { box-sizing: border-box; margin: 0; padding: 0; }
  html, body {
    width: 1200px; height: 873px; overflow: hidden;
    background: var(--bg);
    font-family: "Open Sans", Arial, sans-serif;
  }
  .stage {
    position: relative; width: 1200px; height: 873px;
  }
  .card {
    position: absolute; top: 278px;
    width: 520px; height: 316px;
    background: var(--card);
    box-shadow: 0 6px 18px rgba(0,0,0,.12);
    overflow: hidden;
  }
  .card--front { left: 53px; }
  .card--back { left: 627px; }

  .card__swoosh { position: absolute; inset: 0; width: 100%; height: 100%; }

  .contact {
    position: absolute; left: 150px; top: 36px;
    color: var(--text-grey);
  }
  .contact__name {
    color: var(--brand-blue); font-weight: 700;
    font-size: 15px; letter-spacing: .5px; text-transform: uppercase;
  }
  .contact__role { font-size: 13px; margin-bottom: 14px; }
  .contact__line {
    display: flex; align-items: center; gap: 8px;
    font-size: 13px; line-height: 22px;
  }
  .contact__line svg { width: 12px; height: 12px; flex: none; }

  .wordmark {
    position: absolute; display: flex; align-items: center; gap: 10px;
    color: var(--brand-slate); font-weight: 700;
    text-transform: uppercase; letter-spacing: 1px; white-space: nowrap;
  }
  .wordmark__square { background: var(--brand-slate); flex: none; }
  .card--front .wordmark { right: 26px; bottom: 118px; font-size: 18px; }
  .card--front .wordmark__square { width: 30px; height: 30px; }
  .card--back .wordmark {
    left: 50%; top: 50%; transform: translate(-50%, -50%); font-size: 30px;
  }
  .card--back .wordmark__square { width: 48px; height: 48px; }
</style>
</head>
<body>
<main class="stage">
  <section class="card card--front" aria-label="Business card front">
    <svg class="card__swoosh" viewBox="0 0 520 316" preserveAspectRatio="none" aria-hidden="true">
      <path d="M0 92 C 60 210, 250 290, 520 296 L520 316 L0 316 Z" fill="var(--brand-slate)"/>
      <path d="M0 104 C 60 218, 250 296, 520 302 L520 316 L0 316 Z" fill="var(--brand-blue)"/>
    </svg>
    <div class="contact">
      <p class="contact__name">Corin Maddox</p>
      <p class="contact__role">General Manager</p>
      <p class="contact__line">
        <svg viewBox="0 0 12 12"><path d="M2.5 1 L4.5 1 L5.2 3.5 L4 4.6 C4.6 6 6 7.4 7.4 8 L8.5 6.8 L11 7.5 L11 9.5 C11 10.3 10.3 11 9.5 11 C5 11 1 7 1 2.5 C1 1.7 1.7 1 2.5 1 Z" fill="var(--icon-blue)"/></svg>
        0400 555 218
      </p>
      <p class="contact__line">
        <svg viewBox="0 0 12 12"><rect x="1" y="2.5" width="10" height="7" fill="none" stroke="var(--icon-blue)" stroke-width="1.2"/><path d="M1 2.5 L6 6.5 L11 2.5" fill="none" stroke="var(--icon-blue)" stroke-width="1.2"/></svg>
        cmaddox@kltroofing.com.au
      </p>
      <p class="contact__line">
        <svg viewBox="0 0 12 12"><path d="M6 11 C3 7.5 2 6 2 4.5 A4 4 0 0 1 10 4.5 C10 6 9 7.5 6 11 Z" fill="var(--icon-blue)"/><circle cx="6" cy="4.5" r="1.4" fill="#fff"/></svg>
        28 Harlow Street, Bayside
      </p>
    </div>
    <div class="wordmark">
      <span class="wordmark__square" aria-hidden="true"></span>
      <span class="wordmark__name">KLT Roofing</span>
    </div>
  </section>

  <section class="card card--back" aria-label="Business card back">
    <div class="wordmark">
      <span class="wordmark__square" aria-hidden="true"></span>
      <span class="wordmark__name">KLT Roofing</span>
    </div>
  </section>
</main>
</body>
</html>
```